Quarrow Rent and Supply Flyer

A4 flyer to send electronic to potential customer via email to tell them about Quarrow Rent.
We are start up company looking at sending companies a flyer to introduce the business.

No Folds required - just a standard A4 design

Target Market(s)

Concrete and construction companies

Industry/Entity Type

Construction Company

Font styles to use
Sans Serif

Colors
fbee3e

Requirements
Must have
• Quarrow Logo
• Images provided
Nice to have
• Black and Yellow colour scheme
Should not have
• n/a

```html
<!DOCTYPE html>
<html lang="en">
<head>
<meta charset="utf-8">
<title>Quarrow Rent and Supply – Flyer</title>
<link href="https://fonts.googleapis.com/css2?family=Michroma&family=Open+Sans:wght@400;600;700&display=swap" rel="stylesheet">
<style>
  :root {
    --yellow: #fcd116;
    --black: #1a1a1a;
    --charcoal: #262626;
    --white: #ffffff;
    --footer-grey: #e9e9e9;
    --stage: #d6d6d6;
    --text-dark: #1c1c1c;
    --photo-a: #6b6460;
    --photo-b: #a83a2a;
    --tool-a: #f1f1f1;
    --tool-b: #c9c9c9;
  }
  * { margin: 0; padding: 0; box-sizing: border-box; }
  html, body { width: 684px; height: 1200px; overflow: hidden; }
  body { background: var(--stage); font-family: "Open Sans", Arial, sans-serif; position: relative; }

  .flyer {
    position: absolute; left: 12px; top: 133px;
    width: 660px; height: 934px; overflow: hidden;
    background: linear-gradient(160deg, #2b2b2b 0%, var(--black) 55%, #222 100%);
    box-shadow: 0 6px 18px rgba(0,0,0,.25);
  }
  .flyer__shapes { position: absolute; inset: 0; }

  .brand {
    position: absolute; left: 32px; top: 46px;
    display: flex; align-items: center; gap: 10px;
    font-family: "Open Sans", Arial, sans-serif; font-weight: 700;
    font-size: 27px; letter-spacing: 1px; color: var(--yellow);
  }
  .brand__square { width: 16px; height: 16px; background: var(--yellow); }

  .headline { position: absolute; left: 24px; top: 148px; color: var(--white); }
  .headline__title {
    font-family: "Michroma", Arial, sans-serif; font-size: 34px; line-height: 40px; letter-spacing: 1px;
  }
  .headline__sub {
    margin-top: 10px; font-family: "Michroma", Arial, sans-serif; font-size: 16px; letter-spacing: 1px; font-weight: 400;
  }
  .headline__tag { margin-top: 2px; font-size: 16px; }

  .section-title {
    position: absolute; left: 24px; font-size: 16px; font-weight: 600; color: var(--text-dark);
  }
  .section-title::after {
    content: ""; display: block; width: 38px; height: 2px; background: var(--text-dark); margin-top: 2px;
  }
  .about-title { top: 356px; }
  .overview-title { top: 470px; }

  .copy { position: absolute; left: 24px; font-size: 10.5px; line-height: 14px; color: var(--text-dark); }
  .copy p { margin-bottom: 14px; }
  .about-copy { top: 394px; width: 270px; }
  .overview-copy { top: 510px; }
  .overview-copy .p1 { width: 272px; }
  .overview-copy .p2 { width: 250px; }
  .overview-copy .p3 { width: 166px; }

  .products { position: absolute; left: 461px; top: 615px; color: var(--white); }
  .products__title { font-size: 16px; font-weight: 600; }
  .products__title::after { content: ""; display: block; width: 22px; height: 2px; background: var(--yellow); margin-top: 3px; }
  .products__list { list-style: none; margin-top: 12px; }
  .products__item { display: flex; align-items: center; gap: 8px; font-size: 13.5px; height: 25.3px; }

  .footer {
    position: absolute; left: 0; top: 854px; width: 660px; height: 80px;
    background: var(--footer-grey); border-bottom: 4px solid var(--yellow);
    font-size: 11.5px; color: var(--text-dark);
  }
  .footer__divider { position: absolute; top: 12px; width: 1px; height: 54px; background: #9a9a9a; }
  .footer__col { position: absolute; top: 14px; }
  .footer__row { display: flex; align-items: flex-start; gap: 8px; margin-bottom: 6px; font-weight: 600; line-height: 14px; }
  .footer__row svg { flex: none; margin-top: 1px; }
  .contact-address { left: 30px; }
  .contact-online { left: 286px; }
  .contact-online .footer__row { margin-bottom: 12px; }
  .social { left: 500px; width: 140px; text-align: center; font-weight: 600; }
  .social__links { display: flex; justify-content: center; gap: 9px; margin-top: 10px; }
  .social__dot { width: 17px; height: 17px; border: 1.5px solid #333; border-radius: 50%; }
</style>
</head>
<body>
<main class="flyer">
  <svg class="flyer__shapes" width="660" height="934" viewBox="0 0 660 934">
    <defs>
      <linearGradient id="photo-tone" x1="0" y1="0" x2="1" y2="1">
        <stop offset="0" stop-color="#9c9894"/>
        <stop offset="0.45" stop-color="var(--photo-b)"/>
        <stop offset="1" stop-color="var(--photo-a)"/>
      </linearGradient>
      <radialGradient id="tool-tone" cx="0.5" cy="0.45" r="0.6">
        <stop offset="0" stop-color="var(--tool-a)"/>
        <stop offset="1" stop-color="var(--tool-b)"/>
      </radialGradient>
    </defs>

    <polygon points="0,342 212,342 352,468 500,345 660,334 660,344 522,358 200,854 0,854" fill="var(--yellow)"/>

    <g role="img" aria-label="Photo of the hire warehouse with concrete grinders, vacuums and cutting equipment on shelves">
      <polygon points="415,0 660,0 660,330 480,342 350,462 215,334" fill="url(#photo-tone)"/>
    </g>

    <polyline points="415,0 215,334 0,334" fill="none" stroke="var(--white)" stroke-width="6"/>
    <polyline points="215,334 350,462" fill="none" stroke="var(--white)" stroke-width="6"/>

    <g>
      <circle cx="457" cy="422" r="68" fill="none" stroke="var(--yellow)" stroke-width="3" stroke-dasharray="300 128"/>
      <circle cx="457" cy="422" r="61" fill="var(--white)"/>
      <circle cx="457" cy="422" r="53" fill="url(#tool-tone)" role="img" aria-label="Concrete floor grinder"/>
    </g>
    <g>
      <circle cx="367" cy="574" r="68" fill="none" stroke="var(--yellow)" stroke-width="3" stroke-dasharray="300 128"/>
      <circle cx="367" cy="574" r="61" fill="var(--white)"/>
      <circle cx="367" cy="574" r="53" fill="url(#tool-tone)" role="img" aria-label="Orange concrete ring saw"/>
    </g>
    <g>
      <circle cx="272" cy="727" r="68" fill="none" stroke="var(--yellow)" stroke-width="3" stroke-dasharray="300 128"/>
      <circle cx="272" cy="727" r="61" fill="var(--white)"/>
      <circle cx="272" cy="727" r="53" fill="url(#tool-tone)" role="img" aria-label="Orange dust extraction vacuum"/>
    </g>
  </svg>

  <div class="brand"><span class="brand__square"></span>QUARROW RENT</div>

  <header class="headline">
    <h1 class="headline__title">LOREM<br>IPSUM</h1>
    <p class="headline__sub">DOLOR SIT AMET</p>
    <p class="headline__tag">consectetur adipiscing elit</p>
  </header>

  <h2 class="section-title about-title">About</h2>
  <div class="copy about-copy">
    <p>Quarrow Rent have you covered with Honing, Polishing, Cutting &amp; Drilling Hire equipment for your concrete or construction job. Consumable products available.</p>
  </div>

  <h2 class="section-title overview-title">Company Overview</h2>
  <div class="copy overview-copy">
    <p class="p1">Quarrow Rent is the region's leading business for the hiring of concrete finishing, surface preparation, repair and maintenance needs.</p>
    <p class="p2">We offer an inclusive rental service for anyone from the DIY concreter to concrete finishers who are looking for top of the line concreting equipment, and who value quality service and advice.</p>
    <p class="p3">Our team really knows (and loves) their concrete applications and is committed to assisting every customer by offering them knowledgeable advice, competitive rental prices, and efficient service. At the end of the day, our goal is to have every customer leave knowing that they have the right equipment to create a beautiful concrete product.</p>
  </div>

  <section class="products">
    <h2 class="products__title">Our Products</h2>
    <ul class="products__list">
      <li class="products__item"><svg width="12" height="12" viewBox="0 0 12 12"><circle cx="6" cy="6" r="5" fill="none" stroke="var(--yellow)" stroke-width="1.3"/><path d="M3.4 6.2l1.8 1.8 3.4-3.6" fill="none" stroke="var(--yellow)" stroke-width="1.4"/></svg>Concrete Grinding</li>
      <li class="products__item"><svg width="12" height="12" viewBox="0 0 12 12"><circle cx="6" cy="6" r="5" fill="none" stroke="var(--yellow)" stroke-width="1.3"/><path d="M3.4 6.2l1.8 1.8 3.4-3.6" fill="none" stroke="var(--yellow)" stroke-width="1.4"/></svg>Concrete Cutting</li>
      <li class="products__item"><svg width="12" height="12" viewBox="0 0 12 12"><circle cx="6" cy="6" r="5" fill="none" stroke="var(--yellow)" stroke-width="1.3"/><path d="M3.4 6.2l1.8 1.8 3.4-3.6" fill="none" stroke="var(--yellow)" stroke-width="1.4"/></svg>Sawing and Drilling</li>
      <li class="products__item"><svg width="12" height="12" viewBox="0 0 12 12"><circle cx="6" cy="6" r="5" fill="none" stroke="var(--yellow)" stroke-width="1.3"/><path d="M3.4 6.2l1.8 1.8 3.4-3.6" fill="none" stroke="var(--yellow)" stroke-width="1.4"/></svg>Dust control- Vacuums</li>
      <li class="products__item"><svg width="12" height="12" viewBox="0 0 12 12"><circle cx="6" cy="6" r="5" fill="none" stroke="var(--yellow)" stroke-width="1.3"/><path d="M3.4 6.2l1.8 1.8 3.4-3.6" fill="none" stroke="var(--yellow)" stroke-width="1.4"/></svg>Demolition</li>
      <li class="products__item"><svg width="12" height="12" viewBox="0 0 12 12"><circle cx="6" cy="6" r="5" fill="none" stroke="var(--yellow)" stroke-width="1.3"/><path d="M3.4 6.2l1.8 1.8 3.4-3.6" fill="none" stroke="var(--yellow)" stroke-width="1.4"/></svg>Trailers</li>
      <li class="products__item"><svg width="12" height="12" viewBox="0 0 12 12"><circle cx="6" cy="6" r="5" fill="none" stroke="var(--yellow)" stroke-width="1.3"/><path d="M3.4 6.2l1.8 1.8 3.4-3.6" fill="none" stroke="var(--yellow)" stroke-width="1.4"/></svg>GENERAL HIRE</li>
    </ul>
  </section>

  <footer class="footer">
    <div class="footer__col contact-address">
      <div class="footer__row">
        <svg width="12" height="14" viewBox="0 0 12 14"><path d="M6 13s4.5-4.6 4.5-7.8A4.5 4.5 0 0 0 1.5 5.2C1.5 8.4 6 13 6 13z" fill="none" stroke="#333" stroke-width="1.3"/><circle cx="6" cy="5.3" r="1.6" fill="#333"/></svg>
        <span>Unit 4, 17 Harrow Ave,<br>Kelton</span>
      </div>
      <div class="footer__row">
        <svg width="12" height="12" viewBox="0 0 12 12"><circle cx="6" cy="6" r="5.3" fill="none" stroke="#333" stroke-width="1.2"/><path d="M4 3.4l1 1.6-.7.8c.4.9 1 1.5 1.9 1.9l.8-.7 1.6 1-.5 1.1c-2.4-.3-4.2-2.1-4.5-4.5z" fill="#333"/></svg>
        <span>+61 400 318 264</span>
      </div>
    </div>
    <span class="footer__divider" style="left:238px"></span>
    <div class="footer__col contact-online">
      <div class="footer__row">
        <svg width="13" height="10" viewBox="0 0 13 10"><rect x=".7" y=".7" width="11.6" height="8.6" fill="none" stroke="#333" stroke-width="1.2"/><path d="M.9 1l5.6 4.4L12.1 1" fill="none" stroke="#333" stroke-width="1.2"/></svg>
        <span>info@quarrowrent.com.au</span>
      </div>
      <div class="footer__row">
        <svg width="12" height="12" viewBox="0 0 12 12"><circle cx="6" cy="6" r="5.3" fill="none" stroke="#333" stroke-width="1.1"/><ellipse cx="6" cy="6" rx="2.4" ry="5.3" fill="none" stroke="#333" stroke-width="1"/><path d="M.8 6h10.4" stroke="#333" stroke-width="1"/></svg>
        <span>www.quarrowrent.com.au</span>
      </div>
    </div>
    <span class="footer__divider" style="left:491px"></span>
    <div class="footer__col social">
      <span>Follow us on</span>
      <div class="social__links">
        <span class="social__dot" aria-label="Social profile"></span>
        <span class="social__dot" aria-label="Social profile"></span>
        <span class="social__dot" aria-label="Social profile"></span>
      </div>
    </div>
  </footer>
</main>
</body>
</html>
```